Create the ONLY Supplement line for Male Entrepreneurs! (Verdant Crest MD)

I need a label designed for a new supplement brand that I am launching.

There are five products so need a design that I can simply change the wording for each individual product

The brand name is called verdant crest MD. The focus is male entrepreneurial health.

Target audience is men 35 to 55.

Concepts: the healthier you are in body the more money you will make in business.

Concept to copy: I want to make a clean minimalistic label mimicking Halvorsen MD (google it and you'll see what I mean)
Updates

Target Market(s)

male entrepreneurs 35-55

Industry/Entity Type

Health Supplement

Colors

Designer to choose colors to be used in the design.

Requirements
Must have
• Modern classy design, similar to Halvorsen MD.
Nice to have
• Highlight that the supplement is Doctor Approved.
Should not have
• No loud colors. Present it as high class.

```html
<!DOCTYPE html>
<html lang="en">
<head>
<meta charset="utf-8">
<title>Verdant Crest MD — Supplement Labels</title>
<link rel="stylesheet" href="https://fonts.googleapis.com/css2?family=Playfair+Display:wght@500&family=Montserrat:wght@300;400&display=swap">
<style>
  :root {
    --canvas: #f2f0ed;
    --label-white: #ecebea;
    --label-white-edge: #dcdad8;
    --amber-dark: #4a2618;
    --amber-mid: #6e3b25;
    --ink: #3b3532;
    --ink-soft: #6f6966;
    --mark-taupe: #5f5550;
    --gold: #e9c063;
    --on-amber: #f4eee9;
    --on-amber-soft: #d9cbc2;
  }
  * { box-sizing: border-box; margin: 0; padding: 0; }
  html, body {
    width: 1200px;
    height: 960px;
    overflow: hidden;
    background: var(--canvas);
  }
  .label-range {
    width: 1200px;
    height: 960px;
    display: flex;
    justify-content: center;
    align-items: center;
    gap: 40px;
  }
  .label {
    position: relative;
    width: 340px;
    height: 400px;
    background: var(--label-white);
    color: var(--ink);
    box-shadow: 0 1px 0 var(--label-white-edge), 0 10px 30px rgba(60, 40, 30, 0.08);
  }
  .label--amber {
    background: linear-gradient(160deg, var(--amber-mid) 0%, var(--amber-dark) 100%);
    color: var(--on-amber);
  }
  .brand {
    position: absolute;
    left: 50px;
    top: 26px;
    width: 240px;
    font-family: "Montserrat", sans-serif;
    font-weight: 400;
    font-size: 22px;
    line-height: 1.2;
    letter-spacing: 0.4px;
    white-space: nowrap;
  }
  .brand-tagline {
    position: absolute;
    left: 50px;
    top: 78px;
    font-family: "Montserrat", sans-serif;
    font-weight: 300;
    font-size: 13px;
    letter-spacing: 0.6px;
    color: var(--ink-soft);
  }
  .label--amber .brand-tagline { color: var(--on-amber-soft); }
  .product-mark {
    position: absolute;
    left: 50px;
    width: 44px;
    height: 44px;
    border-radius: 50%;
    background: var(--mark-taupe);
  }
  .label--amber .product-mark { background: var(--gold); }
  .product-block {
    position: absolute;
    left: 50px;
    width: 240px;
  }
  .product-name {
    font-family: "Playfair Display", serif;
    font-weight: 500;
    font-size: 31px;
    line-height: 1.15;
    padding-bottom: 4px;
    border-bottom: 1.5px solid var(--ink);
  }
  .label--amber .product-name { border-bottom-color: var(--gold); }
  .product-name--bare { border-bottom: none; padding-bottom: 0; }
  .product-claim {
    margin-top: 8px;
    font-family: "Montserrat", sans-serif;
    font-weight: 300;
    font-size: 13px;
    line-height: 1.4;
    color: var(--ink-soft);
  }
  .claim-rule {
    margin-top: 28px;
    border-top: 1.5px solid var(--ink);
  }
  .product-meta {
    margin-top: 10px;
    font-family: "Montserrat", sans-serif;
    font-weight: 300;
    font-size: 14px;
    line-height: 1.4;
    color: var(--ink-soft);
  }
  .label--amber .product-meta { color: var(--on-amber-soft); }
</style>
</head>
<body>
<main class="label-range">

  <article class="label label--amber">
    <h1 class="brand">Verdant Crest MD</h1>
    <p class="brand-tagline">ENTREPRENEURIAL HEALTH</p>
    <span class="product-mark" style="top: 196px;"></span>
    <div class="product-block" style="top: 282px;">
      <h2 class="product-name">Omega 3</h2>
      <p class="product-meta">Dietary Supplement<br>90 softgels</p>
    </div>
  </article>

  <article class="label">
    <h1 class="brand">Verdant Crest MD</h1>
    <p class="brand-tagline">ENTREPRENEURIAL HEALTH</p>
    <span class="product-mark" style="top: 196px;"></span>
    <div class="product-block" style="top: 282px;">
      <h2 class="product-name">Omega 3</h2>
      <p class="product-meta">Dietary Supplement<br>90 softgels</p>
    </div>
  </article>

  <article class="label">
    <h1 class="brand">Verdant Crest MD</h1>
    <p class="brand-tagline">ENTREPRENEURIAL HEALTH</p>
    <span class="product-mark" style="top: 118px;"></span>
    <div class="product-block" style="top: 192px;">
      <h2 class="product-name product-name--bare">Multivitamin</h2>
      <p class="product-claim">a stronger body each day<br>builds a sharper mind for<br>every deal you close</p>
      <div class="claim-rule"></div>
      <p class="product-meta">Dietary Supplement<br>90 softgels</p>
    </div>
  </article>

</main>
</body>
</html>
```